Website for the new investment company.

We are building a website for a new company. This will be an investment company. The name of the company is Tern Harbor Equity, or THE. We don't have a company logo yet, so happy to take suggestions on that as well (and will add that to the final cost). The investors of this company will exclusively be Dunmore College alumni graduates. The investors are not students, but instead older professionals in various industries, that previously graduated from the Dunmore College. This company will establish an investment fund and invest in multiple businesses.
The purpose of the website will be to educate Dunmore alumni on the investment fund.
We are looking for:
1. The design to be relatable, but not the copy of the Dunmore College website. https://www.dunmorecol.edu/
2. This is an investment website and must mimic other similar websites
https://plovergate-fund.com/
https://www.brindlevest.com/
https://kestowholdings.com/site/global/home/p_home.gsp
3. Project timeline. We are focused on receiving a design in the next two weeks and then finishing the website over the following 2 weeks. We anticipate paying for additional work and customization after the designs are provided.
4. Website Pages:
1) Homepage - Mission and Objective (high quality photos along with text that we will provide after selecting the winning design)
2) Background - Text and biographies on the 2 founders (high quality photos along with text that we will provide after selecting the winning design)
3) Advisory Board - Text and biographies on the investment Fund's 3 advisory board members (high quality photos along with text that we will provide after selecting the winning design)
4) Fund I - Text and information on the specific investment fund including pictures and biographies of the investment committee (high quality photos along with text that we will provide after selecting the winning design)
5) Contact Us - Typical website contact page for visitors

Target Market(s)

Dunmore Alumni graduates

Industry/Entity Type

Investment

Coding

Coded - Design and coding required

Font styles to use
Serif
Sans Serif

Colors
0054AA
0677BA
7BADD7
CADEEF
E8F1F8

Requirements
Must have
• Must look like other private investment websites as provided in project description
Nice to have
• Mimics the Dunmore College style, but definitely needs to be different. This company has no direct relationship with Dunmore College.
Should not have
• No commercial transactions, no credit card payments etc. Do not replicate any logos, designs or proprietary content from Dunmore College.

```html
<!DOCTYPE html>
<html lang="en">
<head>
<meta charset="utf-8">
<title>Background | Tern Harbor Equity</title>
<link rel="stylesheet" href="https://fonts.googleapis.com/css2?family=Libre+Baskerville:wght@400;700&family=Open+Sans:wght@400;600;700&display=swap">
<style>
  :root {
    --navy: #0a2f6b;
    --blue-deep: #0054AA;
    --blue: #0677BA;
    --blue-mid: #7BADD7;
    --blue-light: #CADEEF;
    --blue-pale: #E8F1F8;
    --white: #ffffff;
    --ink: #2c3a4d;
    --serif: "Libre Baskerville", Georgia, serif;
    --sans: "Open Sans", Arial, sans-serif;
  }
  * { box-sizing: border-box; margin: 0; padding: 0; }
  html, body { width: 828px; height: 1200px; overflow: hidden; background: var(--white); }
  body { font-family: var(--sans); color: var(--ink); position: relative; }

  .hero {
    position: absolute; left: 0; top: 0; width: 828px; height: 236px;
    background: linear-gradient(180deg, #0b2c63 0%, #0f4a93 45%, #1966b3 100%);
  }
  .hero__backdrop {
    position: absolute; inset: 0;
    background:
      linear-gradient(180deg, rgba(10,40,95,0.2) 0%, rgba(10,40,95,0) 50%, rgba(20,90,170,0.55) 100%),
      linear-gradient(90deg, #0a2a5e 0%, #145aa6 50%, #0a2a5e 100%);
    opacity: 0.9;
  }
  .brand {
    position: absolute; left: 34px; top: 26px;
    display: flex; align-items: center; gap: 7px;
    font-family: var(--sans); font-weight: 700; font-size: 11px;
    color: var(--white); letter-spacing: 0.4px;
  }
  .brand__mark { width: 11px; height: 11px; background: var(--white); }
  .nav {
    position: absolute; left: 306px; top: 38px;
    display: flex; align-items: center; gap: 14px;
    font-size: 7.5px; font-weight: 700; letter-spacing: 0.5px; color: var(--white);
  }
  .nav__item--active { background: var(--white); color: var(--blue-deep); padding: 4px 7px; }
  .nav__search { width: 10px; height: 10px; }
  .hero__title {
    position: absolute; left: 0; right: 0; top: 104px; text-align: center;
    font-family: var(--serif); font-weight: 700; font-size: 34px; color: var(--white);
  }

  .tagline {
    position: absolute; left: 0; right: 0; top: 264px; text-align: center;
    font-family: var(--serif); font-weight: 700; font-size: 18px; color: var(--blue-deep);
  }

  .founder { position: absolute; left: 0; width: 828px; }
  .founder--first { top: 316px; height: 286px;
    background: linear-gradient(90deg, var(--white) 0%, var(--blue-pale) 40%, var(--blue-light) 100%); }
  .founder--second { top: 602px; height: 226px;
    background: linear-gradient(90deg, var(--blue-light) 0%, var(--blue-pale) 55%, var(--white) 100%); }
  .founder__photo { position: absolute; }
  .founder--first .founder__photo { left: 40px; top: 0; width: 300px; height: 286px;
    background: linear-gradient(135deg, #3a3f4a 0%, #1e2330 60%, #4b5262 100%); }
  .founder--second .founder__photo { left: 420px; top: 0; width: 408px; height: 226px;
    background: linear-gradient(135deg, #5a1c2e 0%, #7a2a3e 45%, #3c1220 100%); }
  .founder__text { position: absolute; }
  .founder--first .founder__text { left: 362px; top: 22px; width: 430px; }
  .founder--second .founder__text { left: 36px; top: 22px; width: 360px; }
  .founder__name {
    font-family: var(--serif); font-weight: 700; font-size: 14px; color: var(--blue-deep);
    margin-bottom: 10px;
  }
  .founder__bio { font-size: 7px; line-height: 1.6; color: var(--ink); margin-bottom: 7px; }

  .statement {
    position: absolute; left: 0; top: 828px; width: 828px; height: 112px;
    background: linear-gradient(180deg, var(--blue) 0%, var(--blue-deep) 60%, #0a4a97 100%);
    display: flex; align-items: center; justify-content: center;
  }
  .statement__text { font-family: var(--serif); font-weight: 700; font-size: 17px; color: var(--white); }

  .footer { position: absolute; left: 0; top: 940px; width: 828px; height: 260px; background: var(--white); }
  .footer__brand {
    position: absolute; left: 0; right: 0; top: 110px;
    display: flex; justify-content: center; align-items: center; gap: 8px;
    font-weight: 700; font-size: 15px; color: var(--blue-deep); letter-spacing: 0.4px;
  }
  .footer__mark { width: 13px; height: 13px; background: var(--blue-deep); }
  .footer__nav {
    position: absolute; left: 34px; top: 184px; display: flex; gap: 16px;
    font-size: 6.5px; font-weight: 700; color: var(--navy); letter-spacing: 0.4px;
  }
  .footer__contact {
    position: absolute; right: 36px; top: 176px; text-align: right;
    font-size: 6px; line-height: 1.7; color: var(--ink);
  }
</style>
</head>
<body>
  <header class="hero">
    <div class="hero__backdrop" role="img" aria-label="Night city skyline photograph in deep blue tones"></div>
    <div class="brand"><span class="brand__mark"></span>Tern Harbor Equity</div>
    <nav class="nav">
      <span>HOME</span>
      <span class="nav__item--active">BACKGROUND</span>
      <span>ADVISORY BOARD</span>
      <span>FUND I</span>
      <span>CONTACT US</span>
      <svg class="nav__search" viewBox="0 0 12 12"><circle cx="5" cy="5" r="3.5" fill="none" stroke="#fff" stroke-width="1.4"/><line x1="7.6" y1="7.6" x2="11" y2="11" stroke="#fff" stroke-width="1.4"/></svg>
    </nav>
    <h1 class="hero__title">Background</h1>
  </header>

  <h2 class="tagline">Where vision meets value, and growth follows.</h2>

  <section class="founder founder--first">
    <div class="founder__photo" role="img" aria-label="Portrait photograph of founder Owen Halloway in a suit"></div>
    <div class="founder__text">
      <h3 class="founder__name">Owen Halloway</h3>
      <p class="founder__bio">Owen Halloway is a seasoned leader with a passion for sustainable investment and a commitment to ethical business practices. With over two decades of experience in the financial sector, Owen has a proven track record of identifying and capitalizing on lucrative investment opportunities. He graduated from Dunmore College with a degree in Economics and went on to earn an MBA from a leading business school, where he sharpened his strategic skills in portfolio management and risk analysis.</p>
      <p class="founder__bio">Owen's dedication to excellence and innovation is the driving force behind Tern Harbor Equity. He believes that true success comes from building long-term relationships with partners, investors and communities. His leadership style is collaborative and focused, ensuring that every investment reflects the values the firm holds. Beyond the office, Owen remains an active supporter of the Dunmore alumni community and a mentor to young professionals.</p>
    </div>
  </section>

  <section class="founder founder--second">
    <div class="founder__text">
      <h3 class="founder__name">Marisol Vantreck</h3>
      <p class="founder__bio">Marisol Vantreck is a dynamic and forward-thinking entrepreneur with a deep understanding of real estate development and business ventures. She earned her degree in Business Administration from Dunmore College and built her early career advising growing companies on strategy, capital planning and responsible expansion across several markets.</p>
      <p class="founder__bio">Marisol's expertise lies in her ability to recognize the potential in emerging markets and innovative ventures. Her strategic mindset and meticulous attention to detail have been instrumental in shaping the firm's approach to sustainable growth, ensuring every opportunity is weighed with care and integrity.</p>
      <p class="founder__bio">Marisol is motivated by her relentless pursuit of excellence and her unwavering dedication to the values that define Tern Harbor Equity, building trust and lasting partnerships.</p>
    </div>
    <div class="founder__photo" role="img" aria-label="Portrait photograph of founder Marisol Vantreck against a deep red backdrop"></div>
  </section>

  <section class="statement">
    <p class="statement__text">Building wealth with a focus on sustainable and ethical growth.</p>
  </section>

  <footer class="footer">
    <div class="footer__brand"><span class="footer__mark"></span>Tern Harbor Equity</div>
    <nav class="footer__nav">
      <span>HOME</span><span>BACKGROUND</span><span>ADVISORY BOARD</span><span>FUND I</span><span>PRIVACY POLICY</span><span>CONTACT US</span>
    </nav>
    <div class="footer__contact">
      2140 Harbor Point Drive, Suite 300, Tern Bay<br>
      Phone: (555) 014-2290<br>
      Email: info@ternharborequity.com
    </div>
  </footer>
</body>
</html>
```